Korvex Systems*

Stationary design including business cards, letter heads, envelops and email signatures using our new logo

Target Market(s)

Innovative Technologies

Industry/Entity Type

Defense Contracting

Font styles to use
Sans Serif

```html
<!DOCTYPE html>
<html lang="en">
<head>
<meta charset="utf-8">
<title>Korvex Systems — Stationery</title>
<link rel="stylesheet" href="https://fonts.googleapis.com/css2?family=Barlow:wght@400;500&family=Barlow+Semi+Condensed:wght@400;600&display=swap">
<style>
:root{
  --backdrop:#7f7f7f;
  --paper:#ffffff;
  --ink:#1c1c1d;
  --text:#2b2b2b;
  --muted:#555555;
  --rule:#3a3a3a;
  --band:#1b1b1c;
  --flap-line:#e6e6e6;
}
*{margin:0;padding:0;box-sizing:border-box}
html,body{width:1200px;height:699px;overflow:hidden;background:var(--backdrop)}
body{position:relative;font-family:"Barlow",sans-serif;color:var(--text)}
.piece{position:absolute;background:var(--paper);overflow:hidden}
.wordmark{position:absolute;font-family:"Barlow Semi Condensed",sans-serif;font-weight:400;color:var(--ink);white-space:nowrap;letter-spacing:.02em}
.band{position:absolute;left:0;right:0;background:var(--band);color:#fff;font-size:6px;padding-left:16px;display:flex;align-items:center}
.contact-list{position:absolute;list-style:none;font-family:"Barlow Semi Condensed",sans-serif}
.contact-list li{display:flex;align-items:center;gap:3px;white-space:nowrap}
.contact-list svg{flex:none}
.address{position:absolute;font-family:"Barlow Semi Condensed",sans-serif;white-space:nowrap}
.address .company{font-weight:600}

/* business card front */
.card-front{left:73px;top:320px;width:243px;height:138px}
.card-front .wordmark{right:21px;top:52px;font-size:10.5px}
.card-front .person{position:absolute;left:16px;top:58px}
.person .name{font-family:"Barlow Semi Condensed",sans-serif;font-weight:600;font-size:8.5px;color:var(--ink);letter-spacing:.02em}
.person .role{font-size:5.4px;color:var(--muted)}
.card-front .rule{position:absolute;left:16px;right:21px;top:78px;border-top:.6px solid var(--rule)}
.card-front .contact-list{left:16px;top:82px;font-size:5.5px;line-height:7px}
.card-front .address{right:21px;top:84px;font-size:5.4px;line-height:7px;text-align:right}
.card-front .band{top:117px;height:12px;font-size:5.6px}

/* business card back */
.card-back{left:73px;top:494px;width:243px;height:138px;background:var(--band)}

/* letterhead */
.letterhead{left:344px;top:59px;width:407px;height:575px;background:#fcfcfc}
.letterhead .wordmark{right:34px;top:86px;font-size:13px}
.letterhead .greeting{position:absolute;left:34px;top:159px;font-size:9.4px;color:var(--muted)}
.letterhead .body{position:absolute;left:34px;right:34px;top:189px;font-size:5.2px;line-height:8.4px;color:var(--muted);text-align:justify}
.letterhead .body p{margin-bottom:8.4px}
.letterhead .closing{position:absolute;left:34px;top:374px;font-size:5.4px;color:var(--muted)}
.letterhead .signature{position:absolute;left:30px;top:387px;width:108px;height:30px;background:linear-gradient(90deg,#f2f2f2,#e9e9e9)}
.letterhead .rule{position:absolute;left:34px;right:34px;top:499px;border-top:.6px solid var(--rule)}
.letterhead .contact-list{left:34px;top:506px;font-size:6.3px;line-height:7.8px}
.letterhead .address{right:34px;top:506px;font-size:6.1px;line-height:7.8px;text-align:right}
.letterhead .band{top:549px;height:12px;padding-left:34px;font-size:6.2px}

/* email signature */
.signature-block{left:782px;top:194px;width:333px;height:85px}
.signature-block .brand-cell{position:absolute;left:0;width:89px;top:23px;height:40px;display:flex;align-items:center;justify-content:center}
.signature-block .brand-cell .wordmark{position:static;font-size:8.6px}
.signature-block .divider{position:absolute;top:23px;height:40px;border-left:.8px solid var(--rule)}
.signature-block .person{position:absolute;left:110px;top:19px}
.signature-block .person .name{font-size:10px}
.signature-block .person .role{font-size:6.6px;color:var(--text)}
.signature-block .address{left:111px;top:42px;font-size:6.4px;line-height:7.8px}
.signature-block .contact-list{left:237px;top:24px;font-size:6.5px;line-height:7.8px}

/* envelope back */
.envelope-back{left:783px;top:308px;width:331px;height:147px;background:transparent}

/* envelope front */
.envelope-front{left:780px;top:485px;width:334px;height:149px}
.envelope-front .wordmark{left:16px;top:52px;font-size:10px}
.envelope-front .rule{position:absolute;left:16px;right:25px;top:87px;border-top:.6px solid var(--rule)}
.envelope-front .address{left:16px;top:93px;font-size:6.2px;line-height:7.7px}
.envelope-front .band{top:122px;height:12px;font-size:6.2px}
</style>
</head>
<body>

<svg width="0" height="0" style="position:absolute" aria-hidden="true">
  <defs>
    <symbol id="icon-phone" viewBox="0 0 10 10"><path d="M2 1l2 2-1 1.3c.6 1.2 1.5 2.1 2.7 2.7L7 6l2 2-1.2 1.4C4.5 9 1 5.5.6 2.2z" fill="currentColor"/></symbol>
    <symbol id="icon-mobile" viewBox="0 0 10 10"><rect x="2.5" y=".5" width="5" height="9" rx=".8" fill="none" stroke="currentColor" stroke-width="1.2"/></symbol>
    <symbol id="icon-fax" viewBox="0 0 10 10"><rect x="2.5" y="1" width="5" height="3" fill="currentColor"/><rect x=".5" y="4.5" width="9" height="4.5" fill="currentColor"/></symbol>
    <symbol id="icon-mail" viewBox="0 0 10 10"><rect x=".5" y="2" width="9" height="6" fill="currentColor"/><path d="M.8 2.3L5 5.5l4.2-3.2" fill="none" stroke="#fff" stroke-width=".8"/></symbol>
    <symbol id="icon-web" viewBox="0 0 10 10"><circle cx="5" cy="5" r="4.5" fill="currentColor"/><path d="M.5 5h9M5 .5c-2 2.5-2 6.5 0 9M5 .5c2 2.5 2 6.5 0 9" fill="none" stroke="#fff" stroke-width=".6"/></symbol>
  </defs>
</svg>

<!-- Business card, front -->
<section class="piece card-front">
  <div class="wordmark">KORVEX SYSTEMS</div>
  <div class="person">
    <div class="name">DANIEL REYES</div>
    <div class="role">President</div>
  </div>
  <div class="rule"></div>
  <ul class="contact-list">
    <li><svg width="4.5" height="4.5"><use href="#icon-phone"/></svg>555-214-7730</li>
    <li><svg width="4.5" height="4.5"><use href="#icon-mobile"/></svg>555-368-1942</li>
    <li><svg width="4.5" height="4.5"><use href="#icon-fax"/></svg>555-402-6618</li>
    <li><svg width="4.5" height="4.5"><use href="#icon-mail"/></svg>info@korvexsystems.com</li>
  </ul>
  <div class="address">
    <div class="company">Korvex Systems LLC</div>
    <div>2140 Ridgeline Drive</div>
    <div>Fairbanks, Alaska 99701</div>
  </div>
  <div class="band">www.korvexsystems.com</div>
</section>

<!-- Business card, back -->
<section class="piece card-back" role="img" aria-label="Dark card back with a repeating brand pattern"></section>

<!-- Letterhead -->
<section class="piece letterhead">
  <div class="wordmark">KORVEX SYSTEMS</div>
  <div class="greeting">Dear Mr. Reyes,</div>
  <div class="body">
    <p>Thank you for meeting with our team last week. We appreciate the time you gave to review our proposal for field communication systems, and we are pleased to share the next steps. Our engineers have prepared a detailed plan covering design, testing and delivery, with clear milestones for each phase of the program. We look forward to your thoughts.</p>
    <p>The attached schedule outlines the hardware units, software modules and support services included in the offer. Each item has been priced with care and reviewed by our compliance office. Please note that all components meet current defense standards and can be adapted to your site needs.</p>
    <p>During the first phase we will install a pilot network at one location and train your staff on daily use. Results from this pilot will guide the wider rollout. Our field team will stay on site for the full period, and a project lead will send you short weekly reports on progress, risks and open questions so that nothing is missed along the way.</p>
    <p>We believe this approach keeps cost and risk low while giving your units tools they can trust. If any part of the plan needs changes, our team is ready to adjust it quickly and meet with you again at a time that suits your schedule.</p>
    <p>Thank you again for your trust in our work. We are glad to answer any questions and hope to begin soon.</p>
  </div>
  <div class="closing">Sincerely,</div>
  <div class="signature" role="img" aria-label="Handwritten signature"></div>
  <div class="rule"></div>
  <ul class="contact-list">
    <li><svg width="5" height="5"><use href="#icon-phone"/></svg>555-214-7730</li>
    <li><svg width="5" height="5"><use href="#icon-mobile"/></svg>555-368-1942</li>
    <li><svg width="5" height="5"><use href="#icon-fax"/></svg>555-402-6618</li>
    <li><svg width="5" height="5"><use href="#icon-mail"/></svg>info@korvexsystems.com</li>
  </ul>
  <div class="address">
    <div class="company">Korvex Systems LLC</div>
    <div>2140 Ridgeline Drive</div>
    <div>Fairbanks, Alaska 99701</div>
  </div>
  <div class="band">www.korvexsystems.com</div>
</section>

<!-- Email signature -->
<section class="piece signature-block">
  <div class="brand-cell"><div class="wordmark">KORVEX SYSTEMS</div></div>
  <div class="divider" style="left:89px"></div>
  <div class="person">
    <div class="name">DANIEL REYES</div>
    <div class="role">President</div>
  </div>
  <div class="address">
    <div class="company">Korvex Systems LLC</div>
    <div>2140 Ridgeline Drive</div>
    <div>Fairbanks, Alaska 99701</div>
  </div>
  <div class="divider" style="left:217px"></div>
  <ul class="contact-list">
    <li><svg width="5" height="5"><use href="#icon-phone"/></svg>555-214-7730</li>
    <li><svg width="5" height="5"><use href="#icon-mobile"/></svg>555-368-1942</li>
    <li><svg width="5" height="5"><use href="#icon-fax"/></svg>555-402-6618</li>
    <li><svg width="5" height="5"><use href="#icon-mail"/></svg>info@korvexsystems.com</li>
    <li><svg width="5" height="5"><use href="#icon-web"/></svg>www.korvexsystems.com</li>
  </ul>
</section>

<!-- Envelope, back -->
<section class="piece envelope-back">
  <svg width="331" height="147" viewBox="0 0 331 147" aria-hidden="true">
    <rect x="0" y="0" width="331" height="147" fill="#ffffff"/>
    <path d="M0 147L128 68M331 147L203 68" stroke="var(--flap-line)" stroke-width=".8" fill="none"/>
    <path d="M0 0H331L320 9 196 78C180 87 152 87 136 78L6 8Z" fill="var(--band)"/>
  </svg>
</section>

<!-- Envelope, front -->
<section class="piece envelope-front">
  <div class="wordmark">KORVEX SYSTEMS</div>
  <div class="rule"></div>
  <div class="address">
    <div>Korvex Systems LLC</div>
    <div>2140 Ridgeline Drive</div>
    <div>Fairbanks, Alaska 99701</div>
  </div>
  <div class="band">www.korvexsystems.com</div>
</section>

</body>
</html>
```